Slide Master for Harrowfield Engines - A Systematic Hedge Fund

We are looking for someone to produce a theme and slide master for us for our investor presentations. I have uploaded a few examples of templates that we would like to have included:
Main Title
Section Title
Slides with just bullet points
Different image/table configurations with bullet points and foot notes
Biographies of different lengths
A disclaimer (no one will read this but it should still look nice and needs to be in the presentations)
I have also uploaded the company logo, business card and colour definitions. Currently we have a blue colour scheme defined, but it would be nice to get a complementary set of colours so that when we have charts with more elements we can just draw from those.
The most important thing is that the slide master must be of general use to us. We arn't looking to have a specific presentation designed for us, but a theme/style that we can apply ourselves to any presentation we need to give in the future. It should have clearly defined guidelines for where content should go (and if this is different with and without footnotes for example). We would also like it to have a similar feel to the logo/business cards, so matt colours, high contrast, but not busy.
I'm excited to see the results!

```html
<!DOCTYPE html>
<html lang="en">
<head>
<meta charset="utf-8">
<title>Harrowfield Engines – Slide Master</title>
<link href="https://fonts.googleapis.com/css2?family=Montserrat:wght@400;500;600;700;800&family=Open+Sans:wght@400;600&display=swap" rel="stylesheet">
<style>
:root{--navy:#1f4b8e;--blue:#2e6cc6;--sky:#8fb0de;--pale:#dfe8f5;--ink:#2a2f3a;--mute:#8a909c;--line:#e3e7ee;--page:#ffffff;--grey:#c9ced6}
*{margin:0;padding:0;box-sizing:border-box}
html,body{width:1200px;height:4208px;overflow:hidden;background:var(--page)}
.canvas{position:relative;width:1200px;height:4208px}
.slide{position:absolute;width:369px;height:209px;background:#fff;overflow:hidden;box-shadow:0 2px 10px rgba(20,40,80,.13);font-family:'Open Sans',sans-serif;color:var(--ink)}
.slide.navy{background:var(--navy);color:#fff}
.content::after{content:"";position:absolute;left:0;right:0;bottom:0;height:2px;background:var(--blue)}
.h{position:absolute;left:13px;top:13px;font:700 10px Montserrat,sans-serif;color:var(--navy)}
.h em{font-style:normal;color:var(--blue);font-weight:600}
.sub{position:absolute;left:13px;top:27px;font:600 4.6px Montserrat,sans-serif;letter-spacing:1.2px;color:var(--blue)}
.mk{position:absolute;right:12px;top:11px;font:700 5.6px/1.15 Montserrat,sans-serif;color:var(--navy);letter-spacing:.6px;text-align:center}
.mk span{display:block;letter-spacing:2.6px;font-size:4px}
.ft{position:absolute;left:13px;right:13px;bottom:6px;display:flex;justify-content:space-between;font:500 3.6px Montserrat,sans-serif;color:var(--mute);letter-spacing:.4px}
.t{font:400 4.2px/1.55 'Open Sans',sans-serif;color:#6b717c}
.lbl{font:700 4.8px/1.3 Montserrat,sans-serif;color:var(--navy)}
.lbl.b{color:var(--blue)}
.abs{position:absolute}
.logo{font-family:Montserrat,sans-serif;font-weight:700;text-align:center;line-height:1;letter-spacing:1px}
.logo .w1{display:block}
.logo .w2{display:block;letter-spacing:.55em;margin-top:.35em}
.logo.n{color:var(--navy)}
.logo.wt{color:#fff}
.photo{position:absolute;background:linear-gradient(135deg,#c9d2de,#7c8797)}
.net{position:absolute;background:radial-gradient(circle at 70% 40%,rgba(143,176,222,.35),rgba(255,255,255,0) 70%)}
.net.dk{background:radial-gradient(circle at 70% 40%,rgba(143,176,222,.28),rgba(31,75,142,0) 70%)}
.ms{position:absolute;left:18px;top:118px;font:800 11px/1.2 Montserrat,sans-serif}
.ms small{display:block;font:600 4.6px Montserrat,sans-serif;letter-spacing:1.5px;color:var(--blue);margin-top:4px}
.navy .ms small{color:var(--sky)}
.num{font:300 22px Montserrat,sans-serif;color:var(--grey)}
.pill{display:inline-block;font:600 3.8px Montserrat,sans-serif;padding:2px 5px;border-radius:1px}
.row{display:flex;gap:8px}
</style>
</head>
<body>
<div class="canvas">

<!-- ===== Showcase ===== -->
<div class="slide content" style="left:29px;top:40px">
  <div class="h">Infographic</div>
  <div class="mk">HARROWFIELD<span>ENGINES</span></div>
  <svg class="abs" style="left:24px;top:48px" width="130" height="130" viewBox="0 0 130 130"><circle cx="65" cy="65" r="50" fill="none" stroke="#dde3ec" stroke-width="1" stroke-dasharray="3 3"/><circle cx="65" cy="65" r="30" fill="#fff" stroke="#e6eaf0"/><circle cx="65" cy="15" r="9" fill="#fff" stroke="#cfd6e1"/><circle cx="108" cy="40" r="11" fill="var(--blue)"/><circle cx="108" cy="90" r="9" fill="#d6dce5"/><circle cx="65" cy="115" r="9" fill="var(--sky)"/></svg>
  <div class="abs lbl" style="left:64px;top:110px;width:50px;text-align:center;font-size:4px">HARROWFIELD ENGINES</div>
  <div class="abs" style="left:190px;top:50px;width:160px">
    <div class="lbl">Content Title</div><div class="t">Get a modern layout that is easy to change.</div><br>
    <div class="lbl b">Content Title</div><div class="t">Get a modern layout that is easy to change.</div><br>
    <div class="lbl">Content Title</div><div class="t">Get a modern layout that is easy to change.</div><br>
    <div class="lbl">Content Title</div><div class="t">Get a modern layout that is easy to change.</div>
  </div>
  <div class="ft"><span>HARROWFIELD ENGINES | 2021</span><span>PAGE | 10</span></div>
</div>

<div class="slide navy" style="left:418px;top:40px">
  <div class="mk" style="color:#fff;top:18px;right:30px;font-size:9px">HARROWFIELD<span>ENGINES</span></div>
  <div class="abs" style="left:22px;top:150px;font:800 30px Montserrat,sans-serif">01</div>
  <div class="abs" style="left:80px;top:156px;font:700 10px Montserrat,sans-serif">SECTION TITLE</div>
  <div class="abs t" style="left:80px;top:170px;color:#bccbe3">Get a modern layout that is easy to change in any way.</div>
</div>

<div class="slide content" style="left:807px;top:40px">
  <div class="h">CEO DIRECTOR</div>
  <div class="sub">HARROWFIELD ENGINES PRESENTATION</div>
  <div class="mk">HARROWFIELD<span>ENGINES</span></div>
  <div class="photo" role="img" aria-label="Portrait photo of the director" style="left:22px;top:50px;width:70px;height:78px"></div>
  <div class="abs lbl" style="left:22px;width:70px;text-align:center;top:136px">NAME HERE</div>
  <div class="abs" style="left:120px;top:48px;width:100px"><div class="lbl">Content Here</div><div class="t">A short profile paragraph goes here and can be edited with ease.</div></div>
  <div class="abs" style="left:240px;top:48px;width:100px"><div class="lbl b">Content Here</div><div class="t">A short profile paragraph goes here and can be edited with ease.</div></div>
  <div class="abs" style="left:120px;top:110px;width:220px;height:5px;background:var(--navy)"></div>
  <div class="abs" style="left:120px;top:119px;width:170px;height:5px;background:var(--blue)"></div>
  <div class="ft"><span>HARROWFIELD ENGINES | 2021</span><span>PAGE | 14</span></div>
</div>

<div class="slide content" style="left:29px;top:290px">
  <div class="net" role="img" aria-label="Faint network line pattern" style="left:0;top:0;width:369px;height:209px"></div>
  <div class="logo n abs" style="left:0;right:0;top:88px;font-size:20px;opacity:.18">HARROWFIELD<span class="w2" style="font-size:9px">ENGINES</span></div>
  <div class="ft"><span>HARROWFIELD ENGINES | 2021</span><span>PAGE | 13</span></div>
</div>

<div class="slide content" style="left:418px;top:290px">
  <div class="h">Your Title Here</div>
  <div class="sub">SUBTITLE GOES HERE</div>
  <div class="mk">HARROWFIELD<span>ENGINES</span></div>
  <div class="abs" style="left:18px;top:52px;width:140px"><div class="lbl">Content Here</div><div class="t">You can simply impress your audience and add a unique zing and appeal to your presentations. Easy to change colors, photos and text. Get a modern layout that is beautifully designed and simple to reuse.</div></div>
  <div class="photo" role="img" aria-label="Photo of a laptop on a desk" style="left:180px;top:48px;width:170px;height:120px"></div>
  <div class="ft"><span>HARROWFIELD ENGINES | 2021</span><span>PAGE | 15</span></div>
</div>

<div class="slide" style="left:807px;top:290px">
  <div class="net" role="img" aria-label="Faint network line pattern" style="left:0;top:0;width:369px;height:209px"></div>
  <div class="logo n abs" style="left:0;right:0;top:82px;font-size:24px">HARROWFIELD<span class="w2" style="font-size:10px">ENGINES</span></div>
</div>

<div class="slide navy" style="left:150px;top:560px;width:900px;height:510px">
  <div class="net dk" role="img" aria-label="Faint network line pattern" style="left:0;top:0;width:900px;height:510px"></div>
  <div class="logo wt abs" style="left:0;right:0;top:210px;font-size:50px">HARROWFIELD<span class="w2" style="font-size:22px;color:var(--sky)">ENGINES</span></div>
  <div class="abs" style="right:26px;top:120px;writing-mode:vertical-rl;font:500 6px Montserrat,sans-serif;letter-spacing:2px;color:#9fb4d6">WWW.HARROWFIELDENGINES.COM</div>
</div>

<!-- ===== Grid ===== -->
<!-- Row 1 -->
<div class="slide" style="left:29px;top:1221px">
  <div class="logo n abs" style="left:0;right:0;top:84px;font-size:19px">HARROWFIELD<span class="w2" style="font-size:8.5px">ENGINES</span></div>
  <div class="abs" style="right:12px;top:50px;writing-mode:vertical-rl;font:500 3.6px Montserrat,sans-serif;letter-spacing:1px;color:var(--mute)">WWW.HARROWFIELDENGINES.COM</div>
</div>
<div class="slide" style="left:418px;top:1221px">
  <div class="logo n abs" style="left:20px;width:150px;top:88px;font-size:13px">HARROWFIELD<span class="w2" style="font-size:6px">ENGINES</span></div>
  <div class="abs" style="left:200px;top:34px;width:1px;height:140px;background:var(--line)"></div>
  <div class="abs" style="left:210px;top:36px;font:700 13px/1.15 Montserrat,sans-serif;color:var(--navy)">HARROWFIELD<br><span style="color:var(--blue)">ENGINES</span><br>PRESENTATION</div>
  <div class="abs" style="left:210px;top:92px;font:600 4.6px Montserrat,sans-serif;letter-spacing:1.5px;color:var(--blue)">SUBTITLE GOES HERE</div>
  <div class="abs t" style="left:210px;top:132px">Month 2021</div>
  <div class="abs pill" style="left:210px;top:150px;border:1px solid var(--navy);color:var(--navy);border-radius:6px">PRESENTER NAME</div>
</div>
<div class="slide" style="left:807px;top:1221px">
  <div class="logo n abs" style="left:0;right:0;top:10px;font-size:7px">HARROWFIELD<span class="w2" style="font-size:3.5px">ENGINES</span></div>
  <div class="abs" style="left:0;right:0;top:40px;height:169px;background:var(--navy)">
    <div class="net dk" role="img" aria-label="Faint network line pattern" style="left:0;top:0;width:369px;height:169px"></div>
    <div class="abs" style="left:0;right:0;top:20px;text-align:center;font:500 4px Montserrat,sans-serif;letter-spacing:1px;color:#c7d4ea">WWW.HARROWFIELDENGINES.COM</div>
    <div class="abs" style="left:0;right:0;top:54px;text-align:center;font:700 13px Montserrat,sans-serif;color:#fff">MASTER SLIDE PRESENTATION</div>
    <div class="abs" style="left:0;right:0;top:74px;text-align:center;font:600 4.6px Montserrat,sans-serif;letter-spacing:1.5px;color:#fff">SUBTITLE GOES HERE</div>
    <div class="abs" style="left:0;right:0;top:104px;text-align:center;font:400 4px Montserrat,sans-serif;color:#c7d4ea">Month 2021</div>
    <div class="abs" style="left:0;right:0;top:124px;text-align:center;font:600 4px Montserrat,sans-serif;letter-spacing:1px;color:#fff">PRESENTER NAME</div>
  </div>
</div>

<!-- Row 2 -->
<div class="slide navy" style="left:29px;top:1451px">
  <div class="logo wt abs" style="left:0;right:0;top:84px;font-size:19px">HARROWFIELD<span class="w2" style="font-size:8.5px;color:var(--sky)">ENGINES</span></div>
  <div class="abs" style="right:12px;top:50px;writing-mode:vertical-rl;font:500 3.6px Montserrat,sans-serif;letter-spacing:1px;color:#9fb4d6">WWW.HARROWFIELDENGINES.COM</div>
</div>
<div class="slide" style="left:418px;top:1451px">
  <div class="net" role="img" aria-label="Faint network line pattern" style="left:0;top:0;width:369px;height:209px"></div>
  <div class="logo n abs" style="left:0;right:0;top:84px;font-size:19px">HARROWFIELD<span class="w2" style="font-size:8.5px">ENGINES</span></div>
  <div class="abs" style="right:12px;top:50px;writing-mode:vertical-rl;font:500 3.6px Montserrat,sans-serif;letter-spacing:1px;color:var(--mute)">WWW.HARROWFIELDENGINES.COM</div>
</div>
<div class="slide content" style="left:807px;top:1451px">
  <div class="h">Table Of Content/Agenda</div>
  <div class="mk">HARROWFIELD<span>ENGINES</span></div>
  <div class="abs" style="left:22px;top:48px;display:grid;grid-template-columns:160px 160px;row-gap:14px">
    <div class="row"><div class="num">1</div><div><div class="lbl">Content here</div><div class="t">Get a modern layout that is easy to change.</div></div></div>
    <div class="row"><div class="num">4</div><div><div class="lbl">Content here</div><div class="t">Get a modern layout that is easy to change.</div></div></div>
    <div class="row"><div class="num">2</div><div><div class="lbl">Content here</div><div class="t">Get a modern layout that is easy to change.</div></div></div>
    <div class="row"><div class="num">5</div><div><div class="lbl">Content here</div><div class="t">Get a modern layout that is easy to change.</div></div></div>
    <div class="row"><div class="num">3</div><div><div class="lbl">Content here</div><div class="t">Get a modern layout that is easy to change.</div></div></div>
    <div class="row"><div class="num">6</div><div><div class="lbl">Content here</div><div class="t">Get a modern layout that is easy to change.</div></div></div>
  </div>
  <div class="ft"><span>HARROWFIELD ENGINES | 2021</span><span>PAGE | 02</span></div>
</div>

<!-- Row 3 -->
<div class="slide" style="left:29px;top:1680px">
  <div class="net" role="img" aria-label="Network line pattern" style="left:150px;top:0;width:219px;height:209px;background:radial-gradient(circle at 70% 55%,rgba(31,75,142,.25),rgba(255,255,255,0) 70%)"></div>
  <div class="logo n abs" style="left:18px;top:32px;font-size:8px;text-align:left">HARROWFIELD<span class="w2" style="font-size:3.6px">ENGINES</span></div>
  <div class="ms" style="color:var(--navy)">MASTER SLIDE<br>PRESENTATION<small>SUBTITLE GOES HERE</small></div>
</div>
<div class="slide navy" style="left:418px;top:1680px">
  <div class="net dk" role="img" aria-label="Network line pattern" style="left:150px;top:0;width:219px;height:209px"></div>
  <div class="logo wt abs" style="left:18px;top:32px;font-size:8px;text-align:left">HARROWFIELD<span class="w2" style="font-size:3.6px">ENGINES</span></div>
  <div class="ms">MASTER SLIDE<br>PRESENTATION<small>SUBTITLE GOES HERE</small></div>
</div>
<div class="slide content" style="left:807px;top:1680px">
  <div class="h">Introduction</div>
  <div class="mk">HARROWFIELD<span>ENGINES</span></div>
  <svg class="abs" style="left:28px;top:80px" width="40" height="40"><circle cx="20" cy="20" r="19" fill="none" stroke="var(--navy)"/><text x="20" y="30" text-anchor="middle" font-family="Montserrat" font-weight="800" font-size="22" fill="var(--blue)">”</text></svg>
  <div class="abs" style="left:100px;top:70px;width:250px;border-left:1px solid var(--line);padding-left:10px"><div class="t">You can simply impress your audience and add a unique zing and appeal to your presentations. Easy to change colors, photos and text. Get a modern layout that is beautifully designed and simple to apply. You can simply impress your audience and add a unique zing to your presentations.</div><div class="t" style="text-align:right;margin-top:4px">— Name here/ Manager</div></div>
  <div class="ft"><span>HARROWFIELD ENGINES | 2021</span><span>PAGE | 03</span></div>
</div>

<!-- Row 4 -->
<div class="slide" style="left:29px;top:1910px">
  <div class="logo n abs" style="left:18px;top:32px;font-size:8px;text-align:left">HARROWFIELD<span class="w2" style="font-size:3.6px">ENGINES</span></div>
  <div class="ms" style="color:var(--navy);top:90px">MASTER SLIDE<br>PRESENTATION<small>SUBTITLE GOES HERE</small></div>
  <div class="abs t" style="left:18px;top:175px">Month 2021</div>
</div>
<div class="slide" style="left:418px;top:1910px">
  <div class="logo n abs" style="left:215px;top:32px;font-size:8px;text-align:left">HARROWFIELD<span class="w2" style="font-size:3.6px">ENGINES</span></div>
  <div class="ms" style="color:var(--navy);left:215px;top:90px">MASTER SLIDE<br>PRESENTATION<small>SUBTITLE GOES HERE</small></div>
  <div class="abs t" style="left:215px;top:175px">Month 2021</div>
</div>
<div class="slide content" style="left:807px;top:1910px">
  <div class="h">Timeline</div>
  <div class="mk">HARROWFIELD<span>ENGINES</span></div>
  <div class="abs lbl" style="left:22px;top:96px;font-size:6px;color:var(--ink)">Start<br><span style="font-weight:400;font-size:4px">Contents</span></div>
  <svg class="abs" style="left:60px;top:96px" width="300" height="30"><line x1="0" y1="12" x2="270" y2="12" stroke="#d7dce4" stroke-dasharray="2 2"/><g fill="#d7dce4"><circle cx="20" cy="12" r="4"/><circle cx="55" cy="12" r="4"/></g><circle cx="95" cy="12" r="4" fill="var(--sky)"/><circle cx="135" cy="12" r="4" fill="var(--blue)"/><circle cx="170" cy="12" r="4" fill="var(--blue)"/><circle cx="210" cy="12" r="4" fill="var(--navy)"/><circle cx="262" cy="12" r="11" fill="var(--navy)"/><text x="262" y="14" text-anchor="middle" font-family="Montserrat" font-size="4.5" font-weight="700" fill="#fff">2021</text></svg>
  <div class="abs lbl" style="left:310px;top:80px;font-size:6px;color:var(--ink)">Vision</div>
  <div class="abs t" style="left:70px;top:62px;width:60px;text-align:center">Get a modern layout. Easy to change.</div>
  <div class="abs t" style="left:150px;top:62px;width:60px;text-align:center">Get a modern layout. Easy to change.</div>
  <div class="abs t" style="left:230px;top:62px;width:60px;text-align:center">Get a modern layout. Easy to change.</div>
  <div class="abs t" style="left:90px;top:132px;width:60px;text-align:center">Get a modern layout. Easy to change.</div>
  <div class="abs t" style="left:190px;top:132px;width:60px;text-align:center">Get a modern layout. Easy to change.</div>
  <div class="ft"><span>HARROWFIELD ENGINES | 2021</span><span>PAGE | 04</span></div>
</div>

<!-- Row 5 -->
<div class="slide content" style="left:29px;top:2139px">
  <div class="h">Your Title Here - One Column</div>
  <div class="mk">HARROWFIELD<span>ENGINES</span></div>
  <div class="abs" style="left:18px;top:52px;width:140px"><div class="lbl">Introduction</div><div class="t" style="margin-top:4px">You can simply impress your audience and add a unique zing and appeal to your presentations. Easy to change colors, photos and text. Get a modern layout that is beautifully designed. You can simply impress your audience and add a unique zing and appeal to your presentations.</div></div>
  <div class="logo n abs" style="left:180px;top:88px;width:170px;font-size:14px;opacity:.14">HARROWFIELD<span class="w2" style="font-size:6px">ENGINES</span></div>
  <div class="ft"><span>HARROWFIELD ENGINES | 2021</span><span>PAGE | 05</span></div>
</div>
<div class="slide content" style="left:418px;top:2139px">
  <div class="h">Your Title Here - Two Column</div>
  <div class="mk">HARROWFIELD<span>ENGINES</span></div>
  <div class="abs" style="left:18px;top:52px;width:150px"><div class="lbl">Content Here</div><div class="t" style="margin-top:4px">You can simply impress your audience and add a unique zing and appeal to your presentations. Easy to change colors, photos and text. Get a modern layout that is beautifully designed.</div></div>
  <div class="abs" style="left:195px;top:52px;width:150px"><div class="lbl b">Content Here</div><div class="t" style="margin-top:4px">You can simply impress your audience and add a unique zing and appeal to your presentations. Easy to change colors, photos and text. Get a modern layout that is beautifully designed.</div></div>
  <div class="ft"><span>HARROWFIELD ENGINES | 2021</span><span>PAGE | 06</span></div>
</div>
<div class="slide content" style="left:807px;top:2139px">
  <div class="h">Your Title Here - Three Column</div>
  <div class="mk">HARROWFIELD<span>ENGINES</span></div>
  <div class="abs" style="left:18px;top:52px;width:100px"><div class="lbl">Content Here</div><div class="t" style="margin-top:4px">You can simply impress your audience and add a unique zing and appeal to your presentations. Easy to change colors, photos and text.</div></div>
  <div class="abs" style="left:133px;top:52px;width:100px"><div class="lbl b">Content Here</div><div class="t" style="margin-top:4px">You can simply impress your audience and add a unique zing and appeal to your presentations. Easy to change colors, photos and text.</div></div>
  <div class="abs" style="left:248px;top:52px;width:100px"><div class="lbl">Content Here</div><div class="t" style="margin-top:4px">You can simply impress your audience and add a unique zing and appeal to your presentations. Easy to change colors, photos and text.</div></div>
  <div class="ft"><span>HARROWFIELD ENGINES | 2021</span><span>PAGE | 07</span></div>
</div>

<!-- Row 6 -->
<div class="slide content" style="left:29px;top:2369px">
  <div class="h">Your Title Here <em>- with foot notes¹</em></div>
  <div class="sub">SUBTITLE GOES HERE</div>
  <div class="mk">HARROWFIELD<span>ENGINES</span></div>
  <div class="abs" style="left:18px;top:48px;width:150px"><div class="t">● You can simply impress your audience and add a unique zing and appeal to your presentations.</div><div class="t" style="margin-top:26px">● You can simply impress your audience and add a unique zing and appeal to your presentations.</div></div>
  <svg class="abs" style="left:185px;top:48px" width="170" height="100"><g stroke="#eef1f5"><line x1="10" y1="10" x2="165" y2="10"/><line x1="10" y1="30" x2="165" y2="30"/><line x1="10" y1="50" x2="165" y2="50"/><line x1="10" y1="70" x2="165" y2="70"/><line x1="10" y1="90" x2="165" y2="90"/></g><polyline fill="none" stroke="var(--navy)" stroke-width="1" points="10,88 25,84 40,80 52,82 65,70 80,66 92,60 105,62 118,48 130,44 142,36 155,30 165,22"/></svg>
  <div class="abs t" style="left:18px;top:178px;width:330px;font-size:3.4px;border-top:1px solid var(--line);padding-top:2px">¹ Footnote text sits here, above the footer line, and can run to two lines of source notes.</div>
  <div class="ft"><span>HARROWFIELD ENGINES | 2021</span><span>PAGE | 08</span></div>
</div>
<div class="slide content" style="left:418px;top:2369px">
  <div class="h">Your Title Here <em>- with foot notes¹</em></div>
  <div class="sub">SUBTITLE GOES HERE</div>
  <div class="mk">HARROWFIELD<span>ENGINES</span></div>
  <div class="abs" style="left:18px;top:48px;width:150px"><div class="t">● You can simply impress your audience and add a unique zing and appeal to your presentations.</div><div class="t" style="margin-top:26px">● You can simply impress your audience and add a unique zing and appeal to your presentations.</div></div>
  <svg class="abs" style="left:185px;top:48px" width="170" height="100"><g stroke="#eef1f5"><line x1="10" y1="10" x2="165" y2="10"/><line x1="10" y1="30" x2="165" y2="30"/><line x1="10" y1="50" x2="165" y2="50"/><line x1="10" y1="70" x2="165" y2="70"/><line x1="10" y1="90" x2="165" y2="90"/></g><polyline fill="none" stroke="var(--navy)" stroke-width="1" points="10,86 25,84 38,76 52,80 65,72 80,64 92,66 105,56 118,50 130,46 142,34 155,32 165,20"/></svg>
  <div class="abs t" style="left:18px;top:178px;width:330px;font-size:3.4px;border-top:1px solid var(--line);padding-top:2px">¹ Footnote text sits here, above the footer line, and can run to two lines of source notes.</div>
  <div class="ft"><span>HARROWFIELD ENGINES | 2021</span><span>PAGE | 09</span></div>
</div>
<div class="slide content" style="left:807px;top:2369px">
  <div class="h">Bullets Points</div>
  <div class="mk">HARROWFIELD<span>ENGINES</span></div>
  <div class="abs" style="left:22px;top:44px;display:grid;grid-template-columns:165px 165px;row-gap:10px">
    <div class="row"><svg width="18" height="18"><circle cx="9" cy="9" r="8" fill="var(--navy)"/><text x="9" y="12" text-anchor="middle" font-family="Montserrat" font-weight="700" font-size="8" fill="#fff">1</text></svg><div><div class="lbl">Content Title here</div><div class="t">Get a modern layout that is easy to change.</div></div></div>
    <div class="row"><svg width="18" height="18"><circle cx="9" cy="9" r="8" fill="var(--navy)"/><text x="9" y="12" text-anchor="middle" font-family="Montserrat" font-weight="700" font-size="8" fill="#fff">4</text></svg><div><div class="lbl">Content Title here</div><div class="t">Get a modern layout that is easy to change.</div></div></div>
    <div class="row"><svg width="18" height="18"><circle cx="9" cy="9" r="8" fill="var(--blue)"/><text x="9" y="12" text-anchor="middle" font-family="Montserrat" font-weight="700" font-size="8" fill="#fff">2</text></svg><div><div class="lbl b">Content Title here</div><div class="t">Get a modern layout that is easy to change.</div></div></div>
    <div class="row"><svg width="18" height="18"><circle cx="9" cy="9" r="8" fill="var(--blue)"/><text x="9" y="12" text-anchor="middle" font-family="Montserrat" font-weight="700" font-size="8" fill="#fff">5</text></svg><div><div class="lbl b">Content Title here</div><div class="t">Get a modern layout that is easy to change.</div></div></div>
    <div class="row"><svg width="18" height="18"><circle cx="9" cy="9" r="8" fill="var(--grey)"/><text x="9" y="12" text-anchor="middle" font-family="Montserrat" font-weight="700" font-size="8" fill="#fff">3</text></svg><div><div class="lbl">Content Title here</div><div class="t">Get a modern layout that is easy to change.</div></div></div>
    <div class="row"><svg width="18" height="18"><circle cx="9" cy="9" r="8" fill="var(--grey)"/><text x="9" y="12" text-anchor="middle" font-family="Montserrat" font-weight="700" font-size="8" fill="#fff">6</text></svg><div><div class="lbl">Content Title here</div><div class="t">Get a modern layout that is easy to change.</div></div></div>
  </div>
  <div class="ft"><span>HARROWFIELD ENGINES | 2021</span><span>PAGE | 10</span></div>
</div>

<!-- Row 7 -->
<div class="slide content" style="left:29px;top:2598px">
  <div class="h">Your Title Here</div>
  <div class="sub">SUBTITLE GOES HERE</div>
  <div class="mk">HARROWFIELD<span>ENGINES</span></div>
  <div class="abs" style="left:18px;top:54px;width:140px"><div class="lbl">Content Here</div><div class="t" style="margin-top:4px">You can simply impress your audience and add a unique zing and appeal to your presentations. Easy to change colors, photos and text. Get a modern layout that is beautifully designed.</div></div>
  <div class="photo" role="img" aria-label="Photo of a laptop on a desk" style="left:180px;top:52px;width:170px;height:115px"></div>
  <svg class="abs" style="left:164px;top:66px" width="26" height="84"><circle cx="13" cy="13" r="10" fill="var(--navy)"/><circle cx="13" cy="42" r="10" fill="var(--blue)"/><circle cx="13" cy="71" r="10" fill="var(--grey)"/></svg>
  <div class="ft"><span>HARROWFIELD ENGINES | 2021</span><span>PAGE | 11</span></div>
</div>
<div class="slide content" style="left:418px;top:2598px">
  <div class="h">CEO DIRECTOR</div>
  <div class="sub">HARROWFIELD ENGINES PRESENTATION</div>
  <div class="mk">HARROWFIELD<span>ENGINES</span></div>
  <div class="photo" role="img" aria-label="Portrait photo of the director" style="left:22px;top:50px;width:70px;height:78px"></div>
  <div class="abs lbl" style="left:22px;width:70px;text-align:center;top:136px">NAME HERE</div>
  <svg class="abs" style="left:35px;top:150px" width="44" height="8"><g fill="none" stroke="var(--mute)" stroke-width=".6"><circle cx="4" cy="4" r="3"/><circle cx="15" cy="4" r="3"/><circle cx="26" cy="4" r="3"/><circle cx="37" cy="4" r="3"/></g></svg>
  <div class="abs" style="left:120px;top:48px;width:100px"><div class="lbl">Content Here</div><div class="t">A short profile paragraph goes here and can be edited with ease.</div></div>
  <div class="abs" style="left:240px;top:48px;width:100px"><div class="lbl b">Content Here</div><div class="t">A short profile paragraph goes here and can be edited with ease.</div></div>
  <div class="abs" style="left:120px;top:112px;width:200px;height:5px;background:var(--navy)"></div><div class="abs t" style="left:326px;top:111px">85%</div>
  <div class="abs" style="left:120px;top:121px;width:160px;height:5px;background:var(--blue)"></div><div class="abs t" style="left:326px;top:120px">70%</div>
  <div class="abs t" style="left:290px;top:165px">name@yourmail.com</div>
  <div class="ft"><span>HARROWFIELD ENGINES | 2021</span><span>PAGE | 12</span></div>
</div>
<div class="slide content" style="left:807px;top:2598px">
  <div class="h">Our Team</div>
  <div class="mk">HARROWFIELD<span>ENGINES</span></div>
  <div class="abs" style="left:22px;top:46px;display:flex;gap:10px">
    <div style="width:72px"><div class="photo" role="img" aria-label="Team member portrait" style="position:relative;width:72px;height:62px"></div><div style="background:var(--navy);color:#fff;font:600 4.4px Montserrat,sans-serif;text-align:center;padding:3px">Member Name</div><div class="lbl" style="text-align:center;font-size:4px;color:var(--mute);margin-top:3px">POSITION</div><div class="t" style="text-align:center">A short line about the role.</div></div>
    <div style="width:72px"><div class="photo" role="img" aria-label="Team member portrait" style="position:relative;width:72px;height:62px"></div><div style="background:var(--blue);color:#fff;font:600 4.4px Montserrat,sans-serif;text-align:center;padding:3px">Member Name</div><div class="lbl" style="text-align:center;font-size:4px;color:var(--mute);margin-top:3px">POSITION</div><div class="t" style="text-align:center">A short line about the role.</div></div>
    <div style="width:72px"><div class="photo" role="img" aria-label="Team member portrait" style="position:relative;width:72px;height:62px"></div><div style="background:var(--navy);color:#fff;font:600 4.4px Montserrat,sans-serif;text-align:center;padding:3px">Member Name</div><div class="lbl" style="text-align:center;font-size:4px;color:var(--mute);margin-top:3px">POSITION</div><div class="t" style="text-align:center">A short line about the role.</div></div>
    <div style="width:72px"><div class="photo" role="img" aria-label="Team member portrait" style="position:relative;width:72px;height:62px"></div><div style="background:var(--sky);color:#fff;font:600 4.4px Montserrat,sans-serif;text-align:center;padding:3px">Member Name</div><div class="lbl" style="text-align:center;font-size:4px;color:var(--mute);margin-top:3px">POSITION</div><div class="t" style="text-align:center">A short line about the role.</div></div>
  </div>
  <div class="ft"><span>HARROWFIELD ENGINES | 2021</span><span>PAGE | 13</span></div>
</div>

<!-- Row 8 -->
<div class="slide content" style="left:29px;top:2828px">
  <div class="h">Your Title Here</div>
  <div class="sub">SUBTITLE GOES HERE</div>
  <div class="mk">HARROWFIELD<span>ENGINES</span></div>
  <div class="abs" style="left:18px;top:50px;display:flex;gap:8px">
    <div style="width:77px;height:110px;border:1px solid var(--line);padding:6px;position:relative"><div style="font:700 11px Montserrat,sans-serif;color:var(--navy)">01</div><div class="t" style="margin-top:4px"><b>Lorem ipsum</b> is simply dummy text of the printing and typesetting industry.</div><div style="position:absolute;left:0;right:0;bottom:0;background:var(--navy);color:#fff;font:600 4.4px Montserrat,sans-serif;text-align:center;padding:3px">Option Name</div></div>
    <div style="width:77px;height:110px;border:1px solid var(--line);padding:6px;position:relative"><div style="font:700 11px Montserrat,sans-serif;color:var(--blue)">02</div><div class="t" style="margin-top:4px"><b>Lorem ipsum</b> is simply dummy text of the printing and typesetting industry.</div><div style="position:absolute;left:0;right:0;bottom:0;background:var(--blue);color:#fff;font:600 4.4px Montserrat,sans-serif;text-align:center;padding:3px">Option Name</div></div>
    <div style="width:77px;height:110px;border:1px solid var(--line);padding:6px;position:relative"><div style="font:700 11px Montserrat,sans-serif;color:var(--sky)">03</div><div class="t" style="margin-top:4px"><b>Lorem ipsum</b> is simply dummy text of the printing and typesetting industry.</div><div style="position:absolute;left:0;right:0;bottom:0;background:var(--sky);color:#fff;font:600 4.4px Montserrat,sans-serif;text-align:center;padding:3px">Option Name</div></div>
    <div style="width:77px;height:110px;border:1px solid var(--line);padding:6px;position:relative"><div style="font:700 11px Montserrat,sans-serif;color:var(--ink)">04</div><div class="t" style="margin-top:4px"><b>Lorem ipsum</b> is simply dummy text of the printing and typesetting industry.</div><div style="position:absolute;left:0;right:0;bottom:0;background:var(--grey);color:#fff;font:600 4.4px Montserrat,sans-serif;text-align:center;padding:3px">Option Name</div></div>
  </div>
  <div class="ft"><span>HARROWFIELD ENGINES | 2021</span><span>PAGE | 14</span></div>
</div>
<div class="slide content" style="left:418px;top:2828px">
  <div class="h">Your Title Here - Infographic</div>
  <div class="mk">HARROWFIELD<span>ENGINES</span></div>
  <svg class="abs" style="left:22px;top:44px" width="130" height="130" viewBox="0 0 130 130"><circle cx="65" cy="65" r="50" fill="none" stroke="#dde3ec" stroke-dasharray="3 3"/><circle cx="65" cy="65" r="30" fill="#fff" stroke="#e6eaf0"/><circle cx="65" cy="15" r="9" fill="#fff" stroke="#cfd6e1"/><circle cx="108" cy="40" r="11" fill="var(--blue)"/><circle cx="108" cy="90" r="9" fill="#d6dce5"/><circle cx="65" cy="115" r="9" fill="var(--sky)"/></svg>
  <div class="abs lbl" style="left:62px;top:104px;width:50px;text-align:center;font-size:4px">HARROWFIELD ENGINES</div>
  <div class="abs" style="left:190px;top:46px;width:160px">
    <div class="lbl">✓ Content Title</div><div class="t">Get a modern layout that is easy to change.</div><br>
    <div class="lbl b">✓ Content Title</div><div class="t">Get a modern layout that is easy to change.</div><br>
    <div class="lbl">✓ Content Title</div><div class="t">Get a modern layout that is easy to change.</div><br>
    <div class="lbl">✓ Content Title</div><div class="t">Get a modern layout that is easy to change.</div>
  </div>
  <div class="ft"><span>HARROWFIELD ENGINES | 2021</span><span>PAGE | 15</span></div>
</div>
<div class="slide content" style="left:807px;top:2828px">
  <div class="h">Pie Charts</div>
  <div class="mk">HARROWFIELD<span>ENGINES</span></div>
  <div class="abs t" style="left:50px;top:36px;width:270px;text-align:center">Get a modern layout that is beautifully designed. Easy to change colors, photos and text.</div>
  <svg class="abs" style="left:40px;top:68px" width="290" height="60" viewBox="0 0 290 60">
    <g transform="rotate(-90 40 30)"><circle cx="40" cy="30" r="22" fill="none" stroke="#e8ecf2" stroke-width="7"/><circle cx="40" cy="30" r="22" fill="none" stroke="var(--navy)" stroke-width="7" stroke-dasharray="94 138"/></g>
    <text x="40" y="33" text-anchor="middle" font-family="Montserrat" font-weight="600" font-size="9" fill="var(--ink)">68%</text>
    <g transform="rotate(-90 145 30)"><circle cx="145" cy="30" r="22" fill="none" stroke="#e8ecf2" stroke-width="7"/><circle cx="145" cy="30" r="22" fill="none" stroke="var(--blue)" stroke-width="7" stroke-dasharray="48 138"/></g>
    <text x="145" y="33" text-anchor="middle" font-family="Montserrat" font-weight="600" font-size="9" fill="var(--blue)">35%</text>
    <g transform="rotate(-90 250 30)"><circle cx="250" cy="30" r="22" fill="none" stroke="#e8ecf2" stroke-width="7"/><circle cx="250" cy="30" r="22" fill="none" stroke="var(--grey)" stroke-width="7" stroke-dasharray="76 138"/></g>
    <text x="250" y="33" text-anchor="middle" font-family="Montserrat" font-weight="600" font-size="9" fill="var(--mute)">55%</text>
  </svg>
  <div class="abs t" style="left:45px;top:136px;width:70px;text-align:center">Get a modern layout, beautifully designed.</div>
  <div class="abs t" style="left:150px;top:136px;width:70px;text-align:center">Get a modern layout, beautifully designed.</div>
  <div class="abs t" style="left:255px;top:136px;width:70px;text-align:center">Get a modern layout, beautifully designed.</div>
  <div class="ft"><span>HARROWFIELD ENGINES | 2021</span><span>PAGE | 16</span></div>
</div>

<!-- Row 9 -->
<div class="slide content" style="left:29px;top:3057px">
  <div class="h">Infographic Style</div>
  <div class="mk">HARROWFIELD<span>ENGINES</span></div>
  <div class="abs" style="left:28px;top:50px;width:100px;height:120px;border:1px solid var(--line);padding:8px">
    <div style="display:flex;align-items:center;gap:3px"><svg width="14" height="14"><circle cx="7" cy="7" r="7" fill="var(--navy)"/><text x="7" y="10" text-anchor="middle" font-family="Montserrat" font-size="8" font-weight="700" fill="#fff">$</text></svg><span style="font:800 24px Montserrat,sans-serif;color:var(--navy)">08</span><span class="pill" style="background:var(--navy);color:#fff">COST</span></div>
    <div style="font:600 8px Montserrat,sans-serif;color:var(--navy);margin-left:24px">Million</div>
    <div class="t" style="text-align:center;margin-top:8px">Get a modern slide deck, beautifully designed.</div>
  </div>
  <div class="abs" style="left:150px;top:48px"><span style="font:700 28px Montserrat,sans-serif;color:var(--blue)">04</span> <span class="pill" style="background:var(--blue);color:#fff">SALE</span><div style="font:600 7px Montserrat,sans-serif;color:var(--blue);margin-left:40px">Million</div></div>
  <div class="abs t" style="left:270px;top:58px;width:70px">Get a modern layout, beautifully designed.</div>
  <div class="abs" style="left:150px;top:118px"><span style="font:700 28px Montserrat,sans-serif;color:var(--grey)">15</span> <span class="pill" style="background:#e8ecf2;color:var(--mute)">PERCENTAGE</span></div>
  <div class="abs t" style="left:270px;top:128px;width:70px">Get a modern layout, beautifully designed.</div>
  <div class="ft"><span>HARROWFIELD ENGINES | 2021</span><span>PAGE | 17</span></div>
</div>
<div class="slide navy" style="left:418px;top:3057px">
  <div class="logo wt abs" style="left:220px;top:22px;width:120px;font-size:8px">HARROWFIELD<span class="w2" style="font-size:3.6px;color:var(--sky)">ENGINES</span></div>
  <div class="abs" style="left:0;right:0;top:140px;height:69px;background:rgba(0,0,0,.08)"></div>
  <div class="abs" style="left:28px;top:150px;font:800 32px Montserrat,sans-serif">01</div>
  <div class="abs" style="left:95px;top:156px;font:700 10px Montserrat,sans-serif">SECTION TITLE</div>
  <div class="abs t" style="left:95px;top:172px;color:#bccbe3">Get a modern layout that is beautifully designed. Easy to change.</div>
</div>
<div class="slide" style="left:807px;top:3057px">
  <div class="net" role="img" aria-label="Faint network line pattern" style="left:0;top:0;width:369px;height:209px"></div>
  <div class="logo n abs" style="left:220px;top:22px;width:120px;font-size:8px">HARROWFIELD<span class="w2" style="font-size:3.6px">ENGINES</span></div>
  <div class="abs" style="left:0;right:0;bottom:0;height:3px;background:var(--navy)"></div>
  <div class="abs" style="left:20px;top:150px;font:800 32px Montserrat,sans-serif;color:var(--navy)">02</div>
  <div class="abs" style="left:95px;top:156px;font:700 10px Montserrat,sans-serif;color:var(--navy)">SECTION TITLE</div>
  <div class="abs t" style="left:95px;top:172px">Get a modern layout that is beautifully designed. Easy to change.</div>
</div>

<!-- Row 10 -->
<div class="slide content" style="left:29px;top:3287px">
  <div class="h">Infographic Style</div>
  <div class="mk">HARROWFIELD<span>ENGINES</span></div>
  <svg class="abs" style="left:135px;top:42px" width="100" height="130" viewBox="0 0 100 100">
    <g fill="none" stroke-width="18" transform="rotate(-90 50 50)">
      <circle cx="50" cy="50" r="32" stroke="var(--navy)" stroke-dasharray="48 200.96"/>
      <circle cx="50" cy="50" r="32" stroke="var(--blue)" stroke-dasharray="48 200.96" stroke-dashoffset="-50"/>
      <circle cx="50" cy="50" r="32" stroke="var(--sky)" stroke-dasharray="48 200.96" stroke-dashoffset="-100"/>
      <circle cx="50" cy="50" r="32" stroke="var(--pale)" stroke-dasharray="49 200.96" stroke-dashoffset="-150"/>
    </g>
  </svg>
  <div class="abs" style="left:22px;top:50px;width:100px;text-align:right"><div class="lbl">Content Title</div><div class="t">Get a modern layout, beautifully designed.</div><br><div class="lbl b">Content Title</div><div class="t">Get a modern layout, beautifully designed.</div><br><div class="lbl">Content Title</div><div class="t">Get a modern layout, beautifully designed.</div></div>
  <div class="abs" style="left:250px;top:50px;width:100px"><div class="lbl">Content Title</div><div class="t">Get a modern layout, beautifully designed.</div><br><div class="lbl b">Content Title</div><div class="t">Get a modern layout, beautifully designed.</div><br><div class="lbl">Content Title</div><div class="t">Get a modern layout, beautifully designed.</div></div>
  <div class="ft"><span>HARROWFIELD ENGINES | 2021</span><span>PAGE | 18</span></div>
</div>
<div class="slide content" style="left:418px;top:3287px">
  <div class="h">SWOT Analysis</div>
  <div class="mk">HARROWFIELD<span>ENGINES</span></div>
  <svg class="abs" style="left:150px;top:58px" width="70" height="100" viewBox="0 0 70 100"><circle cx="35" cy="20" r="13" fill="#fff" stroke="var(--navy)" stroke-width="3"/><circle cx="57" cy="50" r="13" fill="#fff" stroke="var(--blue)" stroke-width="3"/><circle cx="13" cy="50" r="13" fill="#fff" stroke="var(--pale)" stroke-width="3"/><circle cx="35" cy="80" r="13" fill="#fff" stroke="var(--grey)" stroke-width="3"/><g font-family="Montserrat" font-weight="700" font-size="10" text-anchor="middle"><text x="35" y="24" fill="var(--navy)">S</text><text x="57" y="54" fill="var(--blue)">W</text><text x="13" y="54" fill="var(--sky)">T</text><text x="35" y="84" fill="var(--mute)">O</text></g></svg>
  <div class="abs" style="left:20px;top:60px;width:115px;text-align:right"><div class="lbl">Strength</div><div class="t">Lorem ipsum dolor sit amet, consectetur adipiscing elit sed do.</div></div>
  <div class="abs" style="left:235px;top:60px;width:115px"><div class="lbl b">Weakness</div><div class="t">Lorem ipsum dolor sit amet, consectetur adipiscing elit sed do.</div></div>
  <div class="abs" style="left:20px;top:120px;width:115px;text-align:right"><div class="lbl" style="color:var(--sky)">Threat</div><div class="t">Lorem ipsum dolor sit amet, consectetur adipiscing elit sed do.</div></div>
  <div class="abs" style="left:235px;top:120px;width:115px"><div class="lbl" style="color:var(--mute)">Opportunity</div><div class="t">Lorem ipsum dolor sit amet, consectetur adipiscing elit sed do.</div></div>
  <div class="ft"><span>HARROWFIELD ENGINES | 2021</span><span>PAGE | 19</span></div>
</div>
<div class="slide content" style="left:807px;top:3287px">
  <div class="h">Bar Chart</div>
  <div class="sub">SUBTITLE GOES HERE</div>
  <div class="mk">HARROWFIELD<span>ENGINES</span></div>
  <div class="abs t" style="left:60px;top:38px;width:280px">Lorem ipsum dolor sit amet, consectetur adipiscing elit. Sed tempor incididunt ut labore.</div>
  <svg class="abs" style="left:18px;top:52px" width="340" height="120" viewBox="0 0 340 120">
    <g font-family="Montserrat" font-size="4" fill="var(--mute)"><text x="0" y="12">100%</text><text x="0" y="37">75%</text><text x="0" y="62">50%</text><text x="0" y="87">25%</text><text x="0" y="110">0%</text></g>
    <g fill="#eceff4"><rect x="30" y="10" width="14" height="98"/><rect x="64" y="10" width="14" height="98"/><rect x="98" y="10" width="14" height="98"/><rect x="132" y="10" width="14" height="98"/><rect x="166" y="10" width="14" height="98"/><rect x="200" y="10" width="14" height="98"/><rect x="234" y="10" width="14" height="98"/><rect x="268" y="10" width="14" height="98"/><rect x="302" y="10" width="14" height="98"/></g>
    <rect x="30" y="88" width="14" height="20" fill="var(--navy)"/><rect x="64" y="70" width="14" height="38" fill="var(--blue)"/><rect x="98" y="60" width="14" height="48" fill="var(--sky)"/><rect x="132" y="80" width="14" height="28" fill="var(--navy)"/><rect x="166" y="50" width="14" height="58" fill="var(--blue)"/><rect x="200" y="40" width="14" height="68" fill="var(--pale)"/><rect x="234" y="74" width="14" height="34" fill="var(--sky)"/><rect x="268" y="58" width="14" height="50" fill="var(--blue)"/><rect x="302" y="36" width="14" height="72" fill="var(--navy)"/>
    <g font-family="Montserrat" font-size="4" fill="var(--mute)" text-anchor="middle"><text x="37" y="116">2011</text><text x="71" y="116">2012</text><text x="105" y="116">2013</text><text x="139" y="116">2014</text><text x="173" y="116">2015</text><text x="207" y="116">2016</text><text x="241" y="116">2017</text><text x="275" y="116">2018</text><text x="309" y="116">2019</text></g>
  </svg>
  <div class="ft"><span>HARROWFIELD ENGINES | 2021</span><span>PAGE | 20</span></div>
</div>

<!-- Row 11 -->
<div class="slide content" style="left:29px;top:3516px">
  <div class="h">Chart with Text</div>
  <div class="mk">HARROWFIELD<span>ENGINES</span></div>
  <svg class="abs" style="left:18px;top:40px" width="200" height="140" viewBox="0 0 200 140">
    <text x="100" y="10" text-anchor="middle" font-family="Montserrat" font-size="5" fill="var(--ink)">Series 1</text>
    <g stroke="#eef1f5"><line x1="15" y1="30" x2="195" y2="30"/><line x1="15" y1="60" x2="195" y2="60"/><line x1="15" y1="90" x2="195" y2="90"/><line x1="15" y1="120" x2="195" y2="120"/></g>
    <g fill="var(--navy)"><rect x="25" y="70" width="8" height="50"/><rect x="43" y="50" width="8" height="70"/><rect x="61" y="80" width="8" height="40"/><rect x="79" y="40" width="8" height="80"/><rect x="97" y="60" width="8" height="60"/><rect x="115" y="35" width="8" height="85"/><rect x="133" y="75" width="8" height="45"/><rect x="151" y="55" width="8" height="65"/><rect x="169" y="45" width="8" height="75"/></g>
  </svg>
  <div class="abs" style="left:240px;top:48px;width:110px;border:1px solid var(--line);padding:6px"><div class="lbl">Content 01</div><div class="t" style="margin-top:3px">You can simply impress your audience and add a unique zing and appeal to your presentations. Easy to change colors, photos and text.</div><div class="t" style="margin-top:10px;text-align:center;font-weight:600">ADD YOUR TEXT HERE</div></div>
  <div class="ft"><span>HARROWFIELD ENGINES | 2021</span><span>PAGE | 21</span></div>
</div>
<div class="slide content" style="left:418px;top:3516px">
  <div class="h">Table Chart - Option 01</div>
  <div class="mk">HARROWFIELD<span>ENGINES</span></div>
  <svg class="abs" style="left:30px;top:42px" width="14" height="130"><g fill="var(--navy)"><circle cx="7" cy="20" r="5"/><circle cx="7" cy="40" r="5"/><circle cx="7" cy="60" r="5"/><circle cx="7" cy="80" r="5"/><circle cx="7" cy="100" r="5"/><circle cx="7" cy="120" r="5"/></g></svg>
  <svg class="abs" style="left:52px;top:42px" width="290" height="130" viewBox="0 0 290 130">
    <rect x="0" y="0" width="95" height="10" fill="var(--navy)"/><rect x="97" y="0" width="95" height="10" fill="var(--blue)"/><rect x="194" y="0" width="95" height="10" fill="var(--navy)"/>
    <g font-family="Montserrat" font-size="4" font-weight="600" fill="#fff" text-anchor="middle"><text x="47" y="6.5">TEXT HERE</text><text x="144" y="6.5">TEXT HERE</text><text x="241" y="6.5">TEXT HERE</text></g>
    <g fill="#f3f5f8"><rect x="0" y="14" width="289" height="12"/><rect x="0" y="54" width="289" height="12"/><rect x="0" y="94" width="289" height="12"/></g>
    <g stroke="#e6eaf0"><line x1="0" y1="30" x2="289" y2="30"/><line x1="0" y1="50" x2="289" y2="50"/><line x1="0" y1="70" x2="289" y2="70"/><line x1="0" y1="90" x2="289" y2="90"/><line x1="0" y1="110" x2="289" y2="110"/></g>
    <g font-family="Open Sans" font-size="4" fill="var(--mute)" text-anchor="middle">
      <text x="47" y="22">Add Contents Title</text><text x="144" y="22">Add Contents Title</text><text x="241" y="22">Add Contents Title</text>
      <text x="47" y="42">Modern Slide Layout</text><text x="144" y="42">Modern Slide Layout</text><text x="241" y="42">Modern Slide Layout</text>
      <text x="47" y="62">Add Contents Title</text><text x="144" y="62">Add Contents Title</text><text x="241" y="62">Add Contents Title</text>
      <text x="47" y="82">Modern Slide Layout</text><text x="144" y="82">Modern Slide Layout</text><text x="241" y="82">Modern Slide Layout</text>
      <text x="47" y="102">Add Contents Title</text><text x="144" y="102">Add Contents Title</text><text x="241" y="102">Add Contents Title</text>
      <text x="47" y="122">Modern Slide Layout</text><text x="144" y="122">Modern Slide Layout</text><text x="241" y="122">Modern Slide Layout</text>
    </g>
  </svg>
  <div class="ft"><span>HARROWFIELD ENGINES | 2021</span><span>PAGE | 22</span></div>
</div>
<div class="slide content" style="left:807px;top:3516px">
  <div class="h">Our Structure</div>
  <div class="mk">HARROWFIELD<span>ENGINES</span></div>
  <svg class="abs" style="left:25px;top:38px" width="140" height="140" viewBox="0 0 140 140">
    <g fill="none" stroke-width="16" transform="rotate(-90 70 70)">
      <circle cx="70" cy="70" r="52" stroke="var(--navy)" stroke-dasharray="163 326.7"/>
      <circle cx="70" cy="70" r="52" stroke="var(--blue)" stroke-dasharray="98 326.7" stroke-dashoffset="-165"/>
      <circle cx="70" cy="70" r="52" stroke="var(--sky)" stroke-dasharray="31 326.7" stroke-dashoffset="-265"/>
      <circle cx="70" cy="70" r="52" stroke="var(--pale)" stroke-dasharray="29 326.7" stroke-dashoffset="-298"/>
    </g>
    <g font-family="Montserrat" font-weight="700" font-size="6" fill="#fff" text-anchor="middle"><text x="18" y="72">50%</text><text x="118" y="60">30%</text><text x="104" y="112">10%</text></g>
    <text x="70" y="72" text-anchor="middle" font-family="Montserrat" font-weight="700" font-size="6" fill="var(--navy)">HARROWFIELD</text>
  </svg>
  <div class="abs" style="left:190px;top:44px;width:160px">
    <div class="t" style="border-bottom:1px solid var(--line);padding:4px 0">● Get a modern slide layout, beautifully designed and easy to change.</div>
    <div class="t" style="border-bottom:1px solid var(--line);padding:4px 0">● Get a modern slide layout, beautifully designed and easy to change.</div>
    <div class="t" style="border-bottom:1px solid var(--line);padding:4px 0">● Get a modern slide layout, beautifully designed and easy to change.</div>
    <div class="t" style="padding:4px 0">● Get a modern slide layout, beautifully designed and easy to change.</div>
  </div>
  <div class="ft"><span>HARROWFIELD ENGINES | 2021</span><span>PAGE | 23</span></div>
</div>

<!-- Row 12 -->
<div class="slide content" style="left:29px;top:3746px">
  <div class="h">Logos with Text</div>
  <div class="mk">HARROWFIELD<span>ENGINES</span></div>
  <div class="abs" style="left:20px;top:54px;display:grid;grid-template-columns:repeat(3,44px);gap:6px 6px">
    <div class="lbl" style="border:1px solid var(--line);padding:6px 2px;text-align:center;color:var(--mute);font-size:4px">Brightmoor</div>
    <div class="lbl" style="border:1px solid var(--line);padding:6px 2px;text-align:center;color:var(--mute);font-size:4px">Brightmoor</div>
    <div class="lbl" style="border:1px solid var(--line);padding:6px 2px;text-align:center;color:var(--mute);font-size:4px">Brightmoor</div>
    <div class="lbl" style="border:1px solid var(--line);padding:6px 2px;text-align:center;color:var(--mute);font-size:4px">Brightmoor</div>
    <div class="lbl" style="border:1px solid var(--line);padding:6px 2px;text-align:center;color:var(--mute);font-size:4px">Brightmoor</div>
    <div class="lbl" style="border:1px solid var(--line);padding:6px 2px;text-align:center;color:var(--mute);font-size:4px">Brightmoor</div>
    <div class="lbl" style="border:1px solid var(--line);padding:6px 2px;text-align:center;color:var(--mute);font-size:4px">Brightmoor</div>
    <div class="lbl" style="border:1px solid var(--line);padding:6px 2px;text-align:center;color:var(--mute);font-size:4px">Brightmoor</div>
    <div class="lbl" style="border:1px solid var(--line);padding:6px 2px;text-align:center;color:var(--mute);font-size:4px">Add Client Logo</div>
  </div>
  <div class="abs" style="left:200px;top:60px;width:150px"><div class="row" style="justify-content:space-between"><div><div class="lbl">Contents Title</div><div class="t">Get a modern layout, easy to change.</div></div><svg width="16" height="16"><circle cx="8" cy="8" r="7" fill="var(--navy)"/><text x="8" y="10" text-anchor="middle" font-family="Montserrat" font-size="5" font-weight="700" fill="#fff">01</text></svg></div></div>
  <div class="abs" style="left:200px;top:110px;width:150px"><div class="row" style="justify-content:space-between"><div><div class="lbl b">Contents Title</div><div class="t">Get a modern layout, easy to change.</div></div><svg width="16" height="16"><circle cx="8" cy="8" r="7" fill="var(--blue)"/><text x="8" y="10" text-anchor="middle" font-family="Montserrat" font-size="5" font-weight="700" fill="#fff">02</text></svg></div></div>
  <div class="ft"><span>HARROWFIELD ENGINES | 2021</span><span>PAGE | 24</span></div>
</div>
<div class="slide content" style="left:418px;top:3746px">
  <div class="photo" role="img" aria-label="Photo of hands signing a document" style="left:0;top:0;width:150px;height:203px;background:linear-gradient(135deg,#3d5f96,#16335f)"></div>
  <div class="abs" style="left:95px;top:12px;font:700 9px Montserrat,sans-serif;color:#fff">Case Study</div>
  <div class="abs t" style="left:12px;top:145px;width:120px;color:#d7e1f0">“Lorem Ipsum is simply dummy text of the printing and typesetting industry, the standard text since the 1500s.”<br><span style="float:right">Name Here</span></div>
  <div class="mk">HARROWFIELD<span>ENGINES</span></div>
  <div class="abs" style="left:165px;top:50px;width:180px">
    <div class="lbl">Challenge</div><div class="t">Get a modern layout, beautifully designed. Easy to change colors.</div><br>
    <div class="lbl b">Solution</div><div class="t">Get a modern layout, beautifully designed. Easy to change colors.</div><br>
    <div class="lbl" style="color:var(--mute)">Result</div><div class="t">Get a modern layout, beautifully designed. Easy to change colors.</div>
  </div>
  <div class="ft" style="left:160px"><span>HARROWFIELD ENGINES | 2021</span><span>PAGE | 25</span></div>
</div>
<div class="slide content" style="left:807px;top:3746px">
  <div class="h">Disclaimer</div>
  <div class="mk">HARROWFIELD<span>ENGINES</span></div>
  <div class="abs" style="left:18px;top:36px;width:333px;font:400 3.2px/1.55 'Open Sans',sans-serif;color:#8b919b;text-align:justify">This document is issued for information only and does not constitute an offer or solicitation to buy or sell any security or interest in any fund. Past performance is not a guide to future returns and the value of investments may fall as well as rise. Any forecasts or targets are opinions only and may change without notice. The material has been prepared from sources believed to be reliable, but no warranty is given as to its accuracy or completeness. This document may not be copied or passed on without prior written consent. Systematic strategies carry model risk, leverage risk and liquidity risk, and investors may lose all of the capital invested. Recipients should seek their own independent advice before making any decision. Nothing here is tax, legal or accounting advice. The information is intended only for professional investors and eligible counterparties and must not be relied upon by any other person.<br><br>This document is issued for information only and does not constitute an offer or solicitation to buy or sell any security or interest in any fund. Past performance is not a guide to future returns and the value of investments may fall as well as rise. Any forecasts or targets are opinions only and may change without notice. The material has been prepared from sources believed to be reliable, but no warranty is given as to its accuracy or completeness. This document may not be copied or passed on without prior written consent. Systematic strategies carry model risk, leverage risk and liquidity risk, and investors may lose all of the capital invested.</div>
  <div class="ft"><span>HARROWFIELD ENGINES | 2021</span><span>PAGE | 26</span></div>
</div>

<!-- Row 13 -->
<div class="slide content" style="left:29px;top:3975px">
  <div class="h">Free Icons</div>
  <div class="mk">HARROWFIELD<span>ENGINES</span></div>
  <div class="abs" role="img" aria-label="Grid of small line icons" style="left:18px;top:36px;width:333px;height:140px;background:repeating-linear-gradient(90deg,#f1f3f7 0 9px,#fff 9px 13px)"></div>
  <div class="ft"><span>HARROWFIELD ENGINES | 2021</span><span>PAGE | 27</span></div>
</div>
<div class="slide navy" style="left:418px;top:3975px">
  <div class="net dk" role="img" aria-label="Faint network line pattern" style="left:0;top:0;width:369px;height:209px"></div>
  <div class="abs" style="left:36px;top:38px;font:700 13px Montserrat,sans-serif">THANK YOU</div>
  <div class="abs" style="left:36px;top:82px;font:600 5px Montserrat,sans-serif;letter-spacing:.6px">PRESENTER NAME</div>
  <div class="abs" style="left:36px;top:100px;font:400 4.4px/2.3 'Open Sans',sans-serif;color:#d3def0">☎ &nbsp;+1 234 567 890<br>◉ &nbsp;www.harrowfieldengines.com<br>✉ &nbsp;ab@yourmail.com<br>⌖ &nbsp;Add your location here</div>
  <div class="logo wt abs" style="left:190px;top:118px;width:150px;font-size:13px">HARROWFIELD<span class="w2" style="font-size:6px;color:var(--sky)">ENGINES</span></div>
</div>
<div class="slide" style="left:807px;top:3975px">
  <div class="net" role="img" aria-label="Faint network line pattern" style="left:0;top:0;width:369px;height:209px"></div>
  <div class="abs" style="left:36px;top:38px;font:700 13px Montserrat,sans-serif;color:var(--navy)">THANK YOU</div>
  <div class="abs" style="left:36px;top:82px;font:600 5px Montserrat,sans-serif;letter-spacing:.6px;color:var(--navy)">PRESENTER NAME</div>
  <div class="abs" style="left:36px;top:100px;font:400 4.4px/2.3 'Open Sans',sans-serif;color:var(--ink)">☎ &nbsp;+1 234 567 890<br>◉ &nbsp;www.harrowfieldengines.com<br>✉ &nbsp;ab@yourmail.com<br>⌖ &nbsp;Add your location here</div>
  <div class="logo n abs" style="left:190px;top:118px;width:150px;font-size:13px">HARROWFIELD<span class="w2" style="font-size:6px">ENGINES</span></div>
</div>

</div>
</body>
</html>
```